Tidewell Outdoor Signage

We need an outdoor signage design for my company with new logo designed from makerhive. We do electrical, Air conditioning & Plumbing, installation, service, repairs and maintenance. The design shall be an eye catching that cannot miss ready it.

Industry/Entity Type

Electrical, Air conditioning, Plumbing

```html
<!DOCTYPE html>
<html lang="en">
<head>
<meta charset="utf-8">
<title>Tidewell Outdoor Signage</title>
<link rel="stylesheet" href="https://fonts.googleapis.com/css2?family=Montserrat:wght@600;700;800;900&family=Anton&display=swap">
<style>
  :root {
    --blue: #1565ad;
    --navy: #0f4f94;
    --orange: #f08a3c;
    --orange-deep: #ee6a1f;
    --red: #e42229;
    --yellow: #f6b21c;
    --sign-bg: #f1f1f2;
    --stage: #d9d9db;
    --white: #ffffff;
  }
  * { margin: 0; padding: 0; box-sizing: border-box; }
  html, body { width: 1200px; height: 720px; overflow: hidden; background: var(--stage); }
  .sign {
    position: absolute; left: 30px; top: 75px; width: 1140px; height: 569px;
    background: linear-gradient(135deg, #f7f7f8 0%, var(--sign-bg) 50%, #fafafa 100%);
    font-family: "Montserrat", sans-serif; overflow: hidden;
  }
  .brand-mark { position: absolute; left: 208px; top: 50px; width: 185px; height: 185px; border-radius: 50%; background: var(--orange); }
  .brand-name { position: absolute; left: 60px; top: 236px; width: 430px; text-align: center; font-size: 104px; font-weight: 700; color: var(--orange); line-height: 1; letter-spacing: -2px; white-space: nowrap; }
  .brand-tagline { position: absolute; left: 60px; top: 336px; width: 430px; text-align: center; font-size: 21px; font-weight: 700; color: var(--navy); white-space: nowrap; }
  .web-pill { position: absolute; left: 68px; top: 386px; width: 466px; height: 49px; border: 2px solid var(--navy); border-radius: 25px; display: flex; align-items: center; justify-content: center; font-size: 21px; font-weight: 700; color: var(--navy); }
  .web-pill .accent { color: var(--orange); }
  .service { position: absolute; left: 646px; width: 464px; height: 52px; border-radius: 0 16px 16px 0; display: flex; align-items: center; padding-left: 30px; font-size: 38px; font-weight: 800; color: var(--white); letter-spacing: 0.3px; white-space: nowrap; }
  .service--electrical { top: 54px; background: var(--blue); }
  .service--air { top: 141px; background: var(--orange); }
  .service--plumbing { top: 226px; background: var(--red); }
  .service-icon { position: absolute; left: 597px; width: 68px; height: 68px; border-radius: 50%; display: flex; align-items: center; justify-content: center; border: 5px solid rgba(255,255,255,0.35); }
  .service-icon--electrical { top: 46px; background: var(--red); }
  .service-icon--air { top: 133px; background: var(--blue); }
  .service-icon--plumbing { top: 218px; background: var(--orange); }
  .offer { position: absolute; left: 603px; top: 304px; font-size: 33px; font-weight: 700; color: var(--navy); line-height: 1.16; white-space: nowrap; }
  .call-band { position: absolute; left: 80px; top: 460px; width: 550px; height: 66px; background: linear-gradient(90deg, var(--red) 0%, var(--orange-deep) 55%, var(--yellow) 100%); clip-path: polygon(0 0, 100% 0, 92% 100%, 0 100%); }
  .call-icon { position: absolute; left: 42px; top: 459px; width: 70px; height: 70px; border-radius: 50%; background: var(--blue); border: 4px solid var(--white); display: flex; align-items: center; justify-content: center; }
  .call-number { position: absolute; left: 122px; top: 448px; font-size: 72px; font-weight: 800; color: var(--white); letter-spacing: -1px; line-height: 1.12; white-space: nowrap; }
  .clock-art { position: absolute; left: 688px; top: 394px; width: 162px; height: 155px; border-radius: 50%; background: linear-gradient(135deg, var(--orange-deep) 0%, var(--red) 55%, var(--yellow) 100%); opacity: 0.85; }
  .hours { position: absolute; left: 596px; top: 398px; font-family: "Anton", sans-serif; font-size: 132px; color: var(--blue); font-style: italic; line-height: 1; letter-spacing: -10px; transform: skewX(-8deg); white-space: nowrap; }
  .hours .slash { color: var(--yellow); }
  .emergency { position: absolute; left: 860px; top: 438px; font-family: "Anton", sans-serif; font-size: 55px; color: var(--navy); line-height: 1; white-space: nowrap; }
  .services-tag { position: absolute; left: 860px; top: 499px; width: 151px; height: 44px; background: var(--red); color: var(--white); font-family: "Anton", sans-serif; font-size: 38px; line-height: 1; display: flex; align-items: center; justify-content: center; }
</style>
</head>
<body>
  <main class="sign">
    <div class="brand-mark"></div>
    <div class="brand-name">Tidewell</div>
    <div class="brand-tagline">Electrical&nbsp; Air Conditioning&nbsp; Plumbing</div>
    <div class="web-pill">www.<span class="accent">Tidewell</span>Electrical.com.au</div>

    <div class="service service--electrical">ELECTRICAL</div>
    <div class="service-icon service-icon--electrical">
      <svg width="30" height="30" viewBox="0 0 24 24"><path d="M13 2 5 14h6l-2 8 9-13h-6z" fill="none" stroke="#fff" stroke-width="1.6" stroke-linejoin="round"/></svg>
    </div>
    <div class="service service--air">AIR CONDITIONING</div>
    <div class="service-icon service-icon--air">
      <svg width="30" height="30" viewBox="0 0 24 24" fill="none" stroke="#fff" stroke-width="1.6" stroke-linecap="round"><path d="M12 2v20M3.3 7l17.4 10M3.3 17 20.7 7"/></svg>
    </div>
    <div class="service service--plumbing">PLUMBING</div>
    <div class="service-icon service-icon--plumbing">
      <svg width="30" height="30" viewBox="0 0 24 24"><path d="M12 3c-4 6-6 9-6 12a6 6 0 0 0 12 0c0-3-2-6-6-12z" fill="none" stroke="#fff" stroke-width="1.6"/></svg>
    </div>

    <p class="offer">Installation, Service, Repairs<br>and Maintenance.</p>

    <div class="call-band"></div>
    <div class="call-icon">
      <svg width="34" height="34" viewBox="0 0 24 24"><path d="M6.6 10.8a15 15 0 0 0 6.6 6.6l2.2-2.2a1 1 0 0 1 1-.25 11.4 11.4 0 0 0 3.6.57 1 1 0 0 1 1 1V20a1 1 0 0 1-1 1A17 17 0 0 1 3 4a1 1 0 0 1 1-1h3.5a1 1 0 0 1 1 1c0 1.25.2 2.45.57 3.57a1 1 0 0 1-.25 1z" fill="none" stroke="#fff" stroke-width="1.5"/></svg>
    </div>
    <div class="call-number">0491 570 156</div>

    <div class="clock-art" role="img" aria-label="Swooping orange clock arrow illustration around the 24/7 figure"></div>
    <div class="hours">24<span class="slash">/</span>7</div>

    <div class="emergency">Emergency</div>
    <div class="services-tag">SERVICES</div>
  </main>
</body>
</html>
```